Greta Polanski Consulting

I am starting my own business and want to have a business card that stands out from the rest. Class is the word i use to describe what i would like to my card to look like.

I see my card as vibrant red card with rounded edges. mat finish
Centered scripted writing
large scripted font: Greta Polanski, smaller font & not scripted: Consulting, next line 0438157226, next line greta@polanskihome.com.au

i have now left 2 email message for the design of my card. Family is spelt wrong on the card. this needs to be correct and finial proof sent though!!! before i can download and approve
Greta

Target Market(s)

Real Estate Professionals

Industry/Entity Type

Business

Contact Information for Business Card

Greta Polanski
Consulting
0438 157 226
greta@polanskihome.com.au

Logo Text

no logo

Requirements
Must have
• must have rounded edges

```html
<!DOCTYPE html>
<html lang="en">
<head>
<meta charset="utf-8">
<title>Greta Polanski Consulting – Business Card</title>
<link href="https://fonts.googleapis.com/css2?family=Herr+Von+Muellerhoff&family=Poiret+One&family=Raleway:wght@400&display=swap" rel="stylesheet">
<style>
  :root {
    --page-bg: #e6e6e6;
    --card-red: #ec3237;
    --ink-white: #ffffff;
  }
  html, body {
    margin: 0;
    padding: 0;
    width: 1200px;
    height: 1000px;
    overflow: hidden;
    background: var(--page-bg);
  }
  .business-card {
    position: absolute;
    left: 100px;
    top: 211px;
    width: 1000px;
    height: 578px;
    border-radius: 58px;
    background: var(--card-red);
    color: var(--ink-white);
    overflow: hidden;
  }
  .card-name {
    position: absolute;
    left: 0;
    width: 100%;
    top: 40px;
    margin: 0;
    text-align: center;
    font-family: "Herr Von Muellerhoff", cursive;
    font-weight: 400;
    font-size: 196px;
    line-height: 1;
    letter-spacing: -2px;
    padding-left: 40px;
    box-sizing: border-box;
  }
  .card-tagline {
    position: absolute;
    right: 198px;
    top: 280px;
    margin: 0;
    font-family: "Poiret One", sans-serif;
    font-size: 52px;
    line-height: 1;
    letter-spacing: 1px;
    text-transform: uppercase;
  }
  .card-phone {
    position: absolute;
    left: 0;
    width: 100%;
    top: 380px;
    margin: 0;
    text-align: center;
    font-family: "Poiret One", sans-serif;
    font-size: 76px;
    line-height: 1;
    letter-spacing: 9px;
    font-weight: 700;
  }
  .card-email {
    position: absolute;
    left: 0;
    width: 100%;
    top: 480px;
    margin: 0;
    text-align: center;
    font-family: "Raleway", sans-serif;
    font-size: 30px;
    line-height: 1;
    letter-spacing: 0.5px;
  }
</style>
</head>
<body>
  <main class="business-card">
    <h1 class="card-name">Greta Polanski</h1>
    <p class="card-tagline">Consulting</p>
    <p class="card-phone">0438 157 226</p>
    <p class="card-email">greta@polanskihome.com.au</p>
  </main>
</body>
</html>
```